New Phone Case requires logo and packaging

We need a nice and sleek logo designed along with packaging for our Premium Phone Case brand

Our Brand Name is Vaxel
Please note this has nothing to do with a Rhino so don't put a Rhino in the logo
I've also attached a file called VAXEL Logo Inspiration, which shows something along the lines of the type of text we want to use. Please note i have photoshopped that image together from another logo we had, and i liked the text, but its for you to see what direction we want to go in. Also note i have shown different variations in that image file, use your imagination with it and show us a nice and clean logo.

We would like the Brand in upper caps such as VAXEL
The brand is for Premium Phone Cases. The first thing that should come to someones mind when looking at the branding is High Quality, Premium and Modern.

The look must be high end and modern

The design must portray high quality and premium!

Also i will say "Less is More". Don't cramp many things on the packaging and logo. We just want a nice, clean cut high quality logo and packaging

I have attached images of an example packaging from a few competitors. One is a standard open from top packaging, while another is a slide out packaging. Our packaging dimensions should be the same which are Packaging dimensions
Length = 18cm
Height = 1.5cm
Depth = 9.5cm

Also note the example packaging has a transparent front section to show which case is inside, this is optional if you want to have it. If not you can cover it all up.

Font styles to use
Other font styles liked:
• Any nice font but just not the standard everyday stuff like Arial, San Serif etc as i want it to be differentiated. A Font that shows Serious Quality and one that stands out would be awesome!

Colors

Designer to choose colors to be used in the design.

Requirements
Must have
• Must be a nice and clean design
• Packaging dimensions
• Length = 18cm
• Height = 1.5cm
• Depth = 9.5cm

```html
<!DOCTYPE html>
<html lang="en">
<head>
<meta charset="utf-8">
<title>Vaxel Packaging Layout</title>
<link rel="stylesheet" href="https://fonts.googleapis.com/css2?family=Montserrat:wght@500;700&family=Open+Sans:wght@400&display=swap">
<style>
  :root {
    --card: #f0e0c9;
    --green: #6fbe44;
    --ink: #000000;
    --note: #8a8a8a;
    --paper: #ffffff;
  }
  html, body {
    margin: 0;
    padding: 0;
    overflow: hidden;
    background: var(--paper);
  }
  .canvas {
    position: relative;
    width: 1200px;
    height: 900px;
    overflow: hidden;
    background: var(--paper);
    font-family: "Open Sans", sans-serif;
  }
  .note {
    position: absolute;
    color: var(--note);
    font-size: 20px;
    font-weight: 400;
    white-space: nowrap;
    line-height: 1;
  }
  .note--stock { right: 90px; top: 26px; }
  .note--front { left: 194px; top: 62px; }
  .note--spine-a { left: 518px; top: 62px; }
  .note--back { left: 723px; top: 62px; }
  .note--spine-b { left: 1041px; top: 62px; }

  .panel {
    position: absolute;
    top: 90px;
    height: 784px;
  }
  .panel--front { left: 86px; width: 415px; background: var(--card); }
  .panel--back { left: 610px; width: 414px; background: var(--card); }
  .panel--spine { width: 66px; background: var(--green); }
  .panel--spine-a { left: 522px; }
  .panel--spine-b { left: 1045px; }

  .front-art {
    position: absolute;
    left: 0;
    top: 0;
  }
  .window-label {
    position: absolute;
    left: 187px;
    top: 98px;
    color: var(--note);
    font-size: 20px;
    white-space: nowrap;
  }
  .brand-name {
    position: absolute;
    left: 71px;
    top: 300px;
    margin: 0;
    font-family: "Montserrat", sans-serif;
    font-weight: 700;
    font-size: 42px;
    letter-spacing: 4px;
    color: var(--green);
    line-height: 1;
  }
  .dot-row {
    position: absolute;
    left: 45px;
    width: 330px;
    display: flex;
    justify-content: space-between;
  }
  .dot-row span {
    width: 4px;
    height: 4px;
    border-radius: 50%;
    background: var(--ink);
  }
  .feature {
    position: absolute;
    left: 0;
    width: 415px;
    margin: 0;
    text-align: center;
    font-family: "Montserrat", sans-serif;
    font-weight: 500;
    font-size: 16px;
    letter-spacing: 2px;
    color: var(--green);
    line-height: 1;
  }
  .spine-name {
    position: absolute;
    left: 50%;
    top: 394px;
    transform: translate(-50%, -50%) rotate(-90deg);
    font-family: "Montserrat", sans-serif;
    font-weight: 700;
    font-size: 42px;
    letter-spacing: 4px;
    color: var(--paper);
    white-space: nowrap;
    line-height: 1;
  }
  .back-note {
    position: absolute;
    left: 0;
    top: 362px;
    width: 414px;
    text-align: center;
    color: var(--note);
    font-size: 20px;
    line-height: 30px;
  }
</style>
</head>
<body>
<div class="canvas">
  <p class="note note--stock" style="margin:0">Packaging made from natural, unbleached card stock</p>
  <p class="note note--front" style="margin:0">[Front of Package]</p>
  <p class="note note--spine-a" style="margin:0">[Spine]</p>
  <p class="note note--back" style="margin:0">[Back of Package]</p>
  <p class="note note--spine-b" style="margin:0">[Spine]</p>

  <section class="panel panel--front">
    <svg class="front-art" width="415" height="784" viewBox="0 0 415 784" aria-hidden="true">
      <path class="front-window" d="M54 42 L366 42 Q372 42 372 48 L372 360 Q372 370 364 362 L52 50 Q47 44 54 42 Z" fill="var(--paper)"/>
      <path class="brand-block" d="M52 124 Q52 118 57 123 L294 360 Q299 364 292 364 L56 364 Q52 364 52 360 Z" fill="var(--ink)"/>
    </svg>
    <span class="window-label">[Front Window]</span>
    <h1 class="brand-name">VAXEL</h1>

    <div class="dot-row" style="top:446px"><span></span><span></span><span></span><span></span><span></span><span></span><span></span><span></span><span></span><span></span><span></span><span></span></div>
    <p class="feature" style="top:486px">FULL PROTECTION</p>
    <div class="dot-row" style="top:535px"><span></span><span></span><span></span><span></span><span></span><span></span><span></span><span></span><span></span><span></span><span></span><span></span></div>
    <p class="feature" style="top:575px">PERFECT FIT</p>
    <div class="dot-row" style="top:624px"><span></span><span></span><span></span><span></span><span></span><span></span><span></span><span></span><span></span><span></span><span></span><span></span></div>
    <p class="feature" style="top:664px">MADE FROM GREEN MATERIALS</p>
    <div class="dot-row" style="top:713px"><span></span><span></span><span></span><span></span><span></span><span></span><span></span><span></span><span></span><span></span><span></span><span></span></div>
  </section>

  <section class="panel panel--spine panel--spine-a">
    <span class="spine-name">VAXEL</span>
  </section>

  <section class="panel panel--back">
    <p class="back-note" style="margin:0">[Technical Specifications<br>&amp; Bar Code]</p>
  </section>

  <section class="panel panel--spine panel--spine-b">
    <span class="spine-name">VAXEL</span>
  </section>
</div>
</body>
</html>
```